Fresh Produce Outlet needs a Poster Design

Hi,
We are Brightleaf Harvest Market, a fruit and veg outlet based in the suburb of Yanchep, Perth, Western Australia.Apart from fresh produce, we also stock nuts and grains, organic products and specialty grocery. We are about to launch a re-branding exercise, projecting ourselves as 'the' shop for fresh produce; quality, taste and freshness being our key differentiators. We are competing against a big supermarket chain who are using marketing muscle power to shut us down and we want to respond with a series of posters which are simple yet bold and sends a clear and positive message to our customers about what we have to offer.
Please feel free to visit our Facebook page www.facebook.com/brightleafharvestmkt to get an idea about our current branding,logo and the shop in general.
Regards
Team - Brightleaf Harvest Market
Target Market(s)
Residents of Yanchep and surrounding suburbs
Industry/Entity Type
Retail
Look and feel

```html
<!DOCTYPE html>
<html lang="en">
<head>
<meta charset="utf-8">
<title>Brightleaf Harvest Market – Poster</title>
<link rel="stylesheet" href="https://fonts.googleapis.com/css2?family=Open+Sans:wdth,wght@75,700;75,800&display=swap">
<style>
  :root {
    --panel-brown: #3d2a1f;
    --text-white: #ffffff;
    --pumpkin-light: #f0a257;
    --pumpkin-mid: #dd7a2c;
    --pumpkin-deep: #b8561a;
    --accent-orange: #e8782a;
  }
  * { margin: 0; padding: 0; box-sizing: border-box; }
  html, body {
    width: 849px;
    height: 1200px;
    overflow: hidden;
    background: #ffffff;
  }
  .poster {
    position: relative;
    width: 849px;
    height: 1200px;
    display: flex;
    font-family: "Open Sans", "Arial Narrow", sans-serif;
    font-stretch: 75%;
  }
  .produce-photo {
    width: 481px;
    height: 100%;
    background:
      radial-gradient(circle at 30% 12%, var(--pumpkin-light) 0, transparent 22%),
      radial-gradient(circle at 75% 35%, var(--pumpkin-light) 0, transparent 20%),
      radial-gradient(circle at 25% 60%, var(--pumpkin-light) 0, transparent 22%),
      radial-gradient(circle at 70% 85%, var(--pumpkin-light) 0, transparent 20%),
      linear-gradient(160deg, var(--pumpkin-mid), var(--pumpkin-deep));
  }
  .message-panel {
    position: relative;
    flex: 1;
    background: var(--panel-brown);
    color: var(--text-white);
    text-align: center;
  }
  .qualities {
    position: absolute;
    top: 104px;
    left: 0;
    right: 0;
    list-style: none;
    font-weight: 800;
    font-size: 44px;
    line-height: 51px;
    letter-spacing: 0.5px;
  }
  .promise {
    position: absolute;
    top: 490px;
    left: 0;
    right: 0;
    font-weight: 800;
    font-size: 44px;
    line-height: 51px;
  }
  .promise .promise-lead {
    display: block;
    font-size: 68px;
    line-height: 72px;
  }
  .brand {
    position: absolute;
    left: 120px;
    top: 1062px;
    display: flex;
    align-items: center;
    gap: 12px;
  }
  .brand-dot {
    width: 30px;
    height: 30px;
    border-radius: 50%;
    background: var(--accent-orange);
    flex: none;
  }
  .brand-name {
    font-weight: 700;
    font-size: 22px;
    line-height: 25px;
    text-align: left;
    color: var(--text-white);
  }
</style>
</head>
<body>
  <main class="poster">
    <div class="produce-photo" role="img" aria-label="Close-up of a pile of bright orange pumpkins with green stems"></div>
    <section class="message-panel">
      <ul class="qualities">
        <li>FRESH.</li>
        <li>TASTY.</li>
        <li>VARIETY.</li>
        <li>COLORFUL.</li>
        <li>ORGANIC.</li>
        <li>HEALTHY.</li>
      </ul>
      <p class="promise">
        <span class="promise-lead">ONLY</span>
        IN ONE<br>PLACE.
      </p>
      <div class="brand">
        <span class="brand-dot"></span>
        <span class="brand-name">Brightleaf Harvest<br>Market</span>
      </div>
    </section>
  </main>
</body>
</html>
```